Label or packaging Design for Hair Care Line

Dear Designer,
We are Corvella, a brand known for our premium hairstyling tools, and we are excited to expand into hair care. We are currently looking for a talented designer to create the label designs for our entire luxury hair care line.
This project is crucial in establishing our visual identity in the hair care market, and we aim to position ourselves alongside premium brands such as LTP, Dorvane Hair Atelier, and Pelmi.
Project Scope
We need a cohesive label design for our hair care line, which includes:
5 products (e.g., shampoo, conditioner, hair oil, styling cream, and a hair mask).
The designs should include:
Front label: Highlighting the product name, key features, and branding.
Our goal is to achieve a design that communicates premium luxury with a touch of professionalism. Below are the specific guidelines to help you align with our vision:
Style and Inspiration
Think of brands like LTP, Dorvane Hair Atelier, and Pelmi.
Luxury and Minimalism: Clean lines, sophisticated typography, and an elegant color palette.
Subtle femininity: premium finishes like metallic accents (gold, silver, or rose gold).
Brand Personality
Premium: Reflecting high quality and exclusivity.
Modern & Professional: Appealing to a refined, professional audience but also suitable for lifestyle-oriented customers.
Warm & Empowering: A brand that celebrates confidence and individuality.
Color Palette
Neutral tones like black, white, accented with metallics (gold or silver) for a luxurious feel.
Colors that feel timeless and elegant rather than trendy or overly bright.
Typography
Use clean, modern fonts (preferably sans-serif or serif for a refined look).
Clear and legible for all product details while maintaining a high-end aesthetic.
Materials and Finishes
Packaging Shape
The label designs should suit a variety of bottle and jar shapes (e.g., cylindrical, flat, or rounded).
Keep scalability in mind so the identity remains consistent across different products.
Deliverables
To understand the aesthetic we are aiming for, here are some brands to use as inspiration:
LTP: For its minimalistic and modern approach.
Dorvane Hair Atelier: For its combination of luxury and professional appeal.
Pelmi: For its soft femininity and lifestyle branding.
we would like to see your designs applied to a variety of packaging types to get an overall impression of how the brand identity works across different product formats. This includes:
A squeeze bottle (e.g., for styling creams or conditioners).
A glass bottle with a dropper (e.g., for a luxurious hair oil).
A shampoo/conditioner bottle (standard pump or flip-top cap).
A spray bottle (e.g., for leave-in treatments or heat protectors).
By creating designs for these different packaging types, we can better evaluate how cohesive and versatile the brand identity will be across the entire product line.

Updates
As you may have noticed from the designs, they don’t quite align with our briefing. The look needs to be clean and professional, similar to Dorvane, LTP, and the other examples we provided. Please address this, and we’ll check it!

Target Market(s)
europe and us
Font styles to use
Other font styles liked:
- century gothic

Look and feel
Each slider illustrates characteristics of the customer's brand and the style your logo design should communicate.

```html
<!DOCTYPE html>
<html lang="en">
<head>
<meta charset="utf-8">
<title>Corvella Hair Care Labels</title>
<link href="https://fonts.googleapis.com/css2?family=Questrial&display=swap" rel="stylesheet">
<style>
  :root {
    --backdrop: #56636f;
    --label-black: #1d1c1f;
    --label-edge: #2a292d;
    --rose: #d98f8c;
    --rose-light: #e9b3ae;
    --rose-dark: #b56f6e;
    --ink-white: #f2f0f0;
    --ink-soft: #cfcccc;
  }
  * { box-sizing: border-box; margin: 0; padding: 0; }
  html, body {
    width: 1200px; height: 721px; overflow: hidden;
    background: var(--backdrop);
    font-family: "Questrial", "Century Gothic", sans-serif;
  }
  .canvas { position: relative; width: 1200px; height: 721px; }

  .label {
    position: absolute;
    background: var(--label-black);
    border: 1px solid var(--label-edge);
    color: var(--ink-white);
    display: flex; flex-direction: column; align-items: center;
    text-align: center;
  }
  .rose-square {
    background: linear-gradient(135deg, var(--rose-dark), var(--rose-light) 45%, var(--rose) 70%, var(--rose-dark));
  }
  .product-name { color: var(--rose); text-transform: uppercase; line-height: 1.2; letter-spacing: 0.02em; }
  .tagline { color: var(--ink-white); }
  .brand-name { color: var(--ink-white); letter-spacing: 0.01em; line-height: 1; }
  .description { color: var(--ink-soft); text-align: justify; text-align-last: center; }
  .volume-row {
    position: absolute; left: 0; right: 0; display: flex; justify-content: space-between;
    color: var(--ink-soft);
  }

  /* Sculpting hair cream */
  .label--cream { left: 70px; top: 120px; width: 230px; height: 480px; padding: 26px 20px 0; }
  .label--cream .rose-square { width: 46px; height: 46px; }
  .label--cream .product-name { font-size: 14px; margin-top: 16px; }
  .label--cream .tagline { font-size: 9px; margin-top: 16px; }
  .label--cream .brand-name { font-size: 36px; margin-top: 62px; }
  .label--cream .description { font-size: 6.4px; line-height: 1.55; margin-top: 40px; }
  .label--cream .volume-row { bottom: 18px; padding: 0 18px; font-size: 6px; }

  /* Luxe hair oil */
  .label--oil { left: 345px; top: 290px; width: 140px; height: 165px; padding: 14px 10px 0; }
  .label--oil .rose-square { width: 26px; height: 20px; }
  .label--oil .product-name { font-size: 7px; margin-top: 7px; }
  .label--oil .tagline { font-size: 5px; margin-top: 6px; }
  .label--oil .brand-name { font-size: 18px; margin-top: 12px; }
  .label--oil .description { font-size: 3.6px; line-height: 1.5; margin-top: 12px; }
  .label--oil .volume-row { bottom: 14px; padding: 0 10px; font-size: 4px; }

  /* Restorative conditioner */
  .label--conditioner { left: 530px; top: 120px; width: 300px; height: 480px; padding: 50px 28px 0; }
  .label--conditioner .rose-square { width: 52px; height: 48px; }
  .label--conditioner .product-name { font-size: 12px; margin-top: 16px; }
  .label--conditioner .tagline { font-size: 8px; margin-top: 18px; }
  .label--conditioner .brand-name { font-size: 36px; margin-top: 42px; }
  .label--conditioner .description { font-size: 7.2px; line-height: 1.65; margin-top: 48px; }
  .label--conditioner .volume-row { bottom: 60px; padding: 0 20px; font-size: 8px; }

  /* Thermal shield spray */
  .label--spray { left: 875px; top: 210px; width: 225px; height: 330px; padding: 20px 20px 0; }
  .label--spray .rose-square { width: 32px; height: 30px; }
  .label--spray .product-name { font-size: 8px; margin-top: 10px; }
  .label--spray .tagline { font-size: 5.5px; margin-top: 10px; }
  .label--spray .brand-name { font-size: 24px; margin-top: 40px; }
  .label--spray .description { font-size: 4.6px; line-height: 1.55; margin-top: 44px; }
  .label--spray .volume-row { bottom: 16px; padding: 0 16px; font-size: 4.5px; }
</style>
</head>
<body>
<main class="canvas">

  <section class="label label--cream">
    <div class="rose-square"></div>
    <h2 class="product-name">Sculpting<br>Hair<br>Cream</h2>
    <p class="tagline">Smooth. Define. Empower.</p>
    <p class="brand-name">corvella</p>
    <p class="description">Elevate your styling routine with our premium sculpting hair cream. This multifunctional cream is designed to add definition, smoothness, and control to your hair while nourishing it from root to tip. Formulated with high-quality ingredients, it tames frizz, enhances shine, and provides long-lasting hold without feeling heavy or sticky. Whether you want a polished, sleek look or soft, natural waves, this cream is your go-to solution for effortless styling.</p>
    <div class="volume-row"><span>200 ml</span><span>6.8 fl. oz.</span></div>
  </section>

  <section class="label label--oil">
    <div class="rose-square"></div>
    <h2 class="product-name">Luxe<br>Hair Oil</h2>
    <p class="tagline">Nourish. Restore. Shine.</p>
    <p class="brand-name">corvella</p>
    <p class="description">A premium hair oil designed to provide deep moisture, instant shine and protection against damage.</p>
    <div class="volume-row"><span>50 ml</span><span>1.7 fl. oz.</span></div>
  </section>

  <section class="label label--conditioner">
    <div class="rose-square"></div>
    <h2 class="product-name">Restorative<br>Conditioner</h2>
    <p class="tagline">Cleanse. Nourish. Rejuvenate.</p>
    <p class="brand-name">corvella</p>
    <p class="description">Indulge your hair with our hydrating shampoo, a luxurious formula that gently cleanses while delivering intense moisture and nourishment. Enriched with premium botanical ingredients, it restores balance to your scalp and hair, leaving it soft, smooth, and manageable. Perfect for daily use and suitable for all hair types, it helps to maintain healthy, vibrant locks.</p>
    <div class="volume-row"><span>300 ml</span><span>10.1 fl. oz.</span></div>
  </section>

  <section class="label label--spray">
    <div class="rose-square"></div>
    <h2 class="product-name">Thermal<br>Shield<br>Spray</h2>
    <p class="tagline">Protect. Strengthen. Style.</p>
    <p class="brand-name">corvella</p>
    <p class="description">Shield your hair from heat damage with our thermal shield spray. A weightless pre-styling treatment for all hair types, it forms a protective barrier against hot tools, reduces frizz and leaves hair smooth and silky.</p>
    <div class="volume-row"><span>150 ml</span><span>5.0 fl. oz.</span></div>
  </section>

</main>
</body>
</html>
```